Velarine Retractable Banner

I need a banner designed to advertise my skincare brand at a meeting. I want it to be eye-catching, yet elegant and modern and it should keep with my branding from my website (www.velarine-example.com). Please let me know if you need any addition files or photos.

I have included the specs for the size I plan to order.

```html
<!DOCTYPE html>
<html lang="en">
<head>
<meta charset="utf-8">
<title>Velarine Retractable Banner</title>
<link rel="stylesheet" href="https://fonts.googleapis.com/css2?family=Gloock&family=Quicksand:wght@500;700&display=swap">
<style>
  :root {
    --page-bg: #e8e6e3;
    --brand-brown: #a0662a;
    --headline-gold: #dca24f;
    --cream: #fbf4ee;
    --product-light: #ffffff;
    --product-shade: #e9e4df;
  }
  * { margin: 0; padding: 0; box-sizing: border-box; }
  html, body {
    width: 671px; height: 1200px; overflow: hidden;
    background: var(--page-bg);
  }
  .banner {
    position: absolute; left: 91px; top: 20px;
    width: 488px; height: 1160px;
    background: var(--brand-brown);
    overflow: hidden;
  }
  .banner__arch { position: absolute; inset: 0; }
  .headline {
    position: absolute; inset: 0;
    font-family: "Gloock", "Georgia", serif;
    font-weight: 400;
    color: var(--headline-gold);
    font-size: 104px; line-height: 1;
    letter-spacing: -1px;
  }
  .headline__line { position: absolute; white-space: nowrap; }
  .headline__line--made { left: 66px;  top: 52px; }
  .headline__line--for  { left: 172px; top: 135px; }
  .headline__line--your { left: 132px; top: 205px; }
  .headline__line--glow { left: 170px; top: 297px; }
  .product-shot {
    position: absolute; left: 78px; top: 440px;
    width: 343px; height: 458px;
    border-radius: 8px;
    background: radial-gradient(ellipse at 50% 55%, var(--product-light) 0%, var(--product-shade) 75%, rgba(233,228,223,0) 100%);
  }
  .brand {
    position: absolute; left: 0; width: 100%; text-align: center;
  }
  .brand__name {
    top: 916px;
    font-family: "Gloock", "Georgia", serif;
    font-size: 80px; line-height: 1;
    letter-spacing: -1px;
    color: var(--brand-brown);
  }
  .brand__byline {
    top: 1000px;
    font-family: "Quicksand", sans-serif;
    font-weight: 500; font-size: 19px; letter-spacing: 1px;
    color: var(--brand-brown);
  }
  .brand__url-wrap { top: 1042px; }
  .brand__url {
    display: inline-block;
    padding: 5px 12px 6px;
    background: var(--brand-brown);
    color: var(--cream);
    font-family: "Quicksand", sans-serif;
    font-weight: 700; font-size: 14px; letter-spacing: 0.5px;
  }
</style>
</head>
<body>
  <main class="banner">
    <svg class="banner__arch" width="488" height="1160" viewBox="0 0 488 1160" aria-hidden="true">
      <path d="M0,698 A288,288 0 0 1 488,698 V1160 H0 Z" fill="var(--cream)"/>
    </svg>

    <h1 class="headline" aria-label="Made for your glow">
      <span class="headline__line headline__line--made">Made</span>
      <span class="headline__line headline__line--for">for</span>
      <span class="headline__line headline__line--your">your</span>
      <span class="headline__line headline__line--glow">glow</span>
    </h1>

    <div class="product-shot" role="img" aria-label="Product photo: white dropper serum bottle, tall pump bottle and exfoliating pad jar"></div>

    <div class="brand brand__name">Velarine</div>
    <div class="brand brand__byline">by dr. elena marsh</div>
    <div class="brand brand__url-wrap"><span class="brand__url">www.velarine-example.com</span></div>
  </main>
</body>
</html>
```